Production Co Needs Movie Poster for Supernatural Thriller

Hi, we need a poster designed for a film we're going to be pitching and raising finance for. The film is a supernatural thriller called "Lanterns Beneath the Stair", a story told from the perspective of the ghosts - a father and his 8 year old son. References include 'When Frost Forgets' (reference poster attached) and 'The Widow's Lantern' - not blood and gore but creepy and atmospheric. We're looking for a design that will capture the imagination and make people want to know more and see the movie!

Synopsis:
When the sudden deaths of young Tobias and his father render them as ghosts, they’re thrust into a dangerous new reality of amateur clairvoyants, determined ghost hunters, and lost souls; a plane of existence where they must survive both the living and the dead.

Industry/Entity Type

Finance

Requirements
Nice to have
• It would be nice to include the father/son imagery perhaps in silhouette. Open to ideas. The film is a psychological thriller as much as a ghost story so it would be good to include that element rather than a 'traditional horror' style poster.
• Alternatively a simple, striking image with the title would also be great - see Velmar poster attached as a reference,
• ALSO - the entire film takes place inside the house.
Should not have
• No screaming faces please.

```html
<!DOCTYPE html>
<html lang="en">
<head>
<meta charset="utf-8">
<title>Lanterns Beneath the Stair — Poster</title>
<link rel="stylesheet" href="https://fonts.googleapis.com/css2?family=Cinzel:wght@400;600&display=swap">
<style>
  :root {
    --ink-parchment: #e8d6ad;
    --ink-reflection: rgba(232, 214, 173, 0.16);
    --stair-amber: #c9773a;
    --stair-glow: #e09a55;
    --stair-rust: #7a3a16;
    --stair-deep: #3a1d0c;
    --riser-line: rgba(20, 10, 4, 0.45);
    --ghost-haze: #a89878;
    --sepia-wash: rgba(160, 140, 100, 0.6);
    --edge-soot: #1c120a;
  }
  * { margin: 0; padding: 0; box-sizing: border-box; }
  html, body {
    width: 800px;
    height: 1200px;
    overflow: hidden;
    background: var(--edge-soot);
  }
  .poster {
    position: relative;
    width: 800px;
    height: 1200px;
    overflow: hidden;
    font-family: "Cinzel", "Trajan Pro", serif;
    color: var(--ink-parchment);
  }
  .staircase,
  .ghost-figures,
  .aged-frame {
    position: absolute;
    inset: 0;
    width: 800px;
    height: 1200px;
  }
  .title-block {
    position: absolute;
    inset: 0;
    font-weight: 400;
  }
  .title-word {
    position: absolute;
    display: block;
    line-height: 1;
    white-space: nowrap;
    text-shadow: 0 0 8px rgba(30, 15, 5, 0.45);
  }
  .title-word::after {
    content: attr(data-word);
    position: absolute;
    left: 0;
    top: 84%;
    transform: scaleY(-1);
    color: var(--ink-reflection);
    text-shadow: none;
    filter: blur(1.2px);
    -webkit-mask-image: linear-gradient(0deg, #000 0%, transparent 55%);
    mask-image: linear-gradient(0deg, #000 0%, transparent 55%);
  }
  .title-lead {
    left: 222px;
    top: 660px;
    font-size: 56px;
    font-variant: small-caps;
    letter-spacing: 1px;
  }
  .title-main {
    left: 50px;
    top: 714px;
    font-size: 140px;
    letter-spacing: -4px;
  }
  .title-link {
    left: 152px;
    top: 956px;
    font-size: 96px;
    font-variant: small-caps;
  }
  .title-close {
    left: 290px;
    top: 893px;
    font-size: 175px;
    letter-spacing: -6px;
  }
</style>
</head>
<body>
  <main class="poster">
    <svg class="staircase" viewBox="0 0 800 1200" aria-hidden="true">
      <defs>
        <pattern id="riser-ribs" width="7" height="10" patternUnits="userSpaceOnUse">
          <rect width="7" height="10" fill="none"/>
          <line x1="1" y1="0" x2="1" y2="10" stroke="var(--riser-line)" stroke-width="1.4"/>
        </pattern>
        <linearGradient id="riser-fill" x1="0" y1="0" x2="0" y2="1">
          <stop offset="0" stop-color="#4a3520"/>
          <stop offset="0.45" stop-color="#6e3518"/>
          <stop offset="0.75" stop-color="#7a3a16"/>
          <stop offset="1" stop-color="#3a1d0c"/>
        </linearGradient>
        <linearGradient id="tread-fill" x1="0" y1="0" x2="1" y2="0">
          <stop offset="0" stop-color="#6a3214"/>
          <stop offset="0.3" stop-color="var(--stair-amber)"/>
          <stop offset="0.55" stop-color="var(--stair-glow)"/>
          <stop offset="0.8" stop-color="var(--stair-amber)"/>
          <stop offset="1" stop-color="#5a2a10"/>
        </linearGradient>
        <linearGradient id="sepia-top" x1="0" y1="0" x2="0" y2="1">
          <stop offset="0" stop-color="var(--sepia-wash)"/>
          <stop offset="0.5" stop-color="rgba(160,140,100,0)"/>
        </linearGradient>
        <radialGradient id="vignette" cx="0.5" cy="0.55" r="0.7">
          <stop offset="0.55" stop-color="rgba(20,12,6,0)"/>
          <stop offset="1" stop-color="rgba(20,12,6,0.85)"/>
        </radialGradient>
      </defs>
      <rect width="800" height="1200" fill="url(#riser-fill)"/>
      <rect width="800" height="1200" fill="url(#riser-ribs)"/>
      <g class="stair-treads" fill="url(#tread-fill)" opacity="0.9">
        <rect x="0" y="60" width="800" height="8"/>
        <rect x="0" y="100" width="800" height="9"/>
        <rect x="0" y="135" width="800" height="10"/>
        <rect x="0" y="170" width="800" height="11"/>
        <rect x="0" y="210" width="800" height="12"/>
        <rect x="0" y="255" width="800" height="14"/>
        <rect x="0" y="312" width="800" height="16"/>
        <rect x="0" y="385" width="800" height="18"/>
        <rect x="0" y="462" width="800" height="22"/>
        <rect x="0" y="548" width="800" height="28"/>
        <rect x="0" y="650" width="800" height="32"/>
        <rect x="0" y="752" width="800" height="34"/>
        <rect x="0" y="860" width="800" height="36"/>
        <rect x="0" y="968" width="800" height="40"/>
        <rect x="0" y="1078" width="800" height="40"/>
        <rect x="0" y="1170" width="800" height="30"/>
      </g>
      <rect width="800" height="1200" fill="url(#sepia-top)"/>
      <rect width="800" height="1200" fill="url(#vignette)"/>
    </svg>

    <svg class="ghost-figures" viewBox="0 0 800 1200" role="img"
         aria-label="Translucent ghostly legs of a father and his young son standing on the upper steps">
      <defs>
        <linearGradient id="ghost-fade" x1="0" y1="0" x2="0" y2="1">
          <stop offset="0" stop-color="var(--ghost-haze)" stop-opacity="0.7"/>
          <stop offset="0.85" stop-color="var(--ghost-haze)" stop-opacity="0.45"/>
          <stop offset="1" stop-color="var(--ghost-haze)" stop-opacity="0"/>
        </linearGradient>
        <filter id="ghost-blur"><feGaussianBlur stdDeviation="14"/></filter>
      </defs>
      <g filter="url(#ghost-blur)" fill="url(#ghost-fade)">
        <rect x="105" y="-20" width="190" height="510" rx="30"/>
        <rect x="395" y="-20" width="150" height="610" rx="30"/>
        <rect x="600" y="-20" width="150" height="600" rx="30"/>
      </g>
    </svg>

    <svg class="aged-frame" viewBox="0 0 800 1200" aria-hidden="true">
      <g fill="none" stroke="rgba(232,214,173,0.35)" stroke-width="2">
        <path d="M14 20 L12 600 L16 1180"/>
        <path d="M786 30 L788 640 L784 1170"/>
        <path d="M20 1182 L400 1178 L780 1184"/>
      </g>
      <g fill="none" stroke="rgba(232,214,173,0.22)" stroke-width="1">
        <path d="M40 1150 L260 1130"/>
        <path d="M560 1110 L760 1060"/>
        <path d="M20 90 L140 70"/>
      </g>
    </svg>

    <h1 class="title-block" aria-label="Lanterns Beneath the Stair">
      <span class="title-word title-lead" data-word="Lanterns">Lanterns</span>
      <span class="title-word title-main" data-word="BENEATH">BENEATH</span>
      <span class="title-word title-close" data-word="STAIR">STAIR</span>
      <span class="title-word title-link" data-word="the">the</span>
    </h1>
  </main>
</body>
</html>
```